Current state of Man's Soul Christian view

I would like an improvement of my design or a reimagining of my design to help people visualize what happens to the soul after we die. The second picture "screenshot 2023" is not my design but gives another idea.

For further information, there are 4 "time" frames that could be sectioned off. Eden is one time. Then adam rebellion and pre messiah earth (with hades/ Sheol). The third time frame is Jesus death, resurrection with the current state of earth. The 4th time frame is the "heavenly realm" which is across all 3 times and is unchanged.

For color ideas, please see my website www.lanternpathnotes.org which has my color theme. But the death of Jesus I would like in some type of red as well as the death of believers.

My goal is something simple, engaging, and easy to understand. If you have any questions please lmk.
Thank you for considering my project.

```html
<!DOCTYPE html>
<html lang="en">
<head>
<meta charset="utf-8">
<title>Current State of Man's Soul</title>
<link rel="stylesheet" href="https://fonts.googleapis.com/css2?family=Montserrat:wght@500;700;800;900&display=swap">
<style>
  :root{
    --red:#e8302c;
    --red-dark:#b81f1c;
    --blue:#1f9ae0;
    --blue-light:#5cbdf0;
    --sky-top:#2fa3e6;
    --sky-bottom:#e8f6fe;
    --ink:#161616;
    --gold:#f3a21f;
    --star:#f7b52a;
    --gray:#e2e2e2;
    --earth-sea:#2e8fd6;
    --earth-land:#63d24a;
    --teal:#26a69a;
    --paper:#ffffff;
  }
  html,body{margin:0;padding:0;overflow:hidden;background:var(--paper);}
  .canvas{width:1200px;height:1200px;display:block;}
  .diagram text{font-family:"Montserrat",Arial,sans-serif;}
  .label{font-weight:700;fill:var(--ink);}
  .label-xl{font-weight:800;fill:var(--ink);font-size:15px;}
  .label-sub{font-weight:600;fill:var(--ink);font-size:10px;}
  .small{font-weight:700;fill:var(--ink);font-size:7px;}
  .white{fill:#fff;}
  .death-text{font-weight:800;fill:#fff;font-size:13px;}
  .vertical{font-weight:800;fill:var(--ink);font-size:13px;letter-spacing:.5px;}
  .flow-blue{fill:none;stroke:var(--blue);stroke-width:2;stroke-dasharray:2 3;}
  .flow-red{fill:none;stroke:var(--red);stroke-width:2;stroke-dasharray:2 3;}
  .arrow-blue{fill:var(--blue);}
  .arrow-red{fill:var(--red);}
</style>
</head>
<body>
<svg class="canvas diagram" viewBox="0 0 960 960" xmlns="http://www.w3.org/2000/svg">
  <defs>
    <linearGradient id="sky" x1="0" y1="0" x2="0" y2="1">
      <stop offset="0" stop-color="var(--sky-top)"/>
      <stop offset="1" stop-color="var(--sky-bottom)"/>
    </linearGradient>
    <linearGradient id="inferno" x1="0" y1="0" x2="0" y2="1">
      <stop offset="0" stop-color="#7a0d0b"/>
      <stop offset=".6" stop-color="#d3261b"/>
      <stop offset="1" stop-color="#f28a1a"/>
    </linearGradient>
    <linearGradient id="comeBar" x1="0" y1="0" x2="0" y2="1">
      <stop offset="0" stop-color="#e6f4fd"/>
      <stop offset="1" stop-color="var(--blue)"/>
    </linearGradient>
    <radialGradient id="globe" cx=".4" cy=".4" r=".7">
      <stop offset="0" stop-color="var(--earth-land)"/>
      <stop offset=".45" stop-color="#3fae5a"/>
      <stop offset="1" stop-color="var(--earth-sea)"/>
    </radialGradient>
    <clipPath id="hadesLeft"><circle cx="335" cy="625" r="52"/></clipPath>
    <clipPath id="hadesRight"><circle cx="745" cy="625" r="52"/></clipPath>
  </defs>

  <!-- Heavenly realm -->
  <g class="heaven">
    <path d="M386 190 H672 A143 125 0 0 1 386 190 Z" fill="url(#sky)" role="img" aria-label="Glowing sky with clouds and doves around the risen Christ on the heavenly throne"/>
    <rect x="458" y="155" width="174" height="20" rx="10" fill="var(--gold)"/>
    <text x="545" y="169.5" text-anchor="middle" class="white" font-weight="800" font-size="12">3RD HEAVEN</text>
    <rect x="438" y="176" width="214" height="16" fill="#fff" stroke="var(--gold)" stroke-width="1"/>
    <text x="545" y="188" text-anchor="middle" class="label" font-size="9.5">GOD'S HEAVENLY THRONE</text>
  </g>

  <!-- Come / Depart axis -->
  <g class="judgement-axis">
    <rect x="542" y="315" width="12" height="310" fill="url(#comeBar)"/>
    <text transform="translate(551 612) rotate(-90)" class="white" font-weight="800" font-size="8">COME</text>
    <path d="M548 308 l-8 10 h16 z" class="arrow-blue"/>
    <rect x="360" y="624" width="360" height="12" fill="var(--gray)"/>
    <rect x="467" y="621" width="166" height="18" rx="9" fill="var(--ink)"/>
    <text x="550" y="634" text-anchor="middle" class="white" font-weight="800" font-size="9.5">JUDGEMENT DAY</text>
    <rect x="542" y="640" width="12" height="45" fill="var(--red)"/>
    <text transform="translate(551 682) rotate(-90)" class="white" font-weight="800" font-size="8">DEPART</text>
    <path d="M540 683 h16 l-8 10 z" class="arrow-red"/>
    <rect x="562" y="590" width="26" height="26" rx="4" fill="var(--teal)" role="img" aria-label="Balance scales of justice"/>
  </g>

  <!-- Hell -->
  <g class="hell">
    <path d="M434 805 A116 108 0 0 1 666 805 Z" fill="url(#inferno)" role="img" aria-label="Fiery underworld with flames and a dark figure"/>
    <rect x="470" y="802" width="160" height="20" rx="10" fill="var(--red)"/>
    <text x="550" y="817" text-anchor="middle" class="white" font-weight="800" font-size="13">HELL</text>
    <text x="550" y="840" text-anchor="middle" class="small" font-size="6.5">ICONS BY PIXELGROVE FROM GLYPHSHELF.COM</text>
  </g>

  <!-- Eden era -->
  <g class="eden">
    <circle cx="115" cy="415" r="48" fill="#fff" stroke="var(--teal)" stroke-width="2.5"/>
    <circle cx="115" cy="415" r="42" fill="#dff1e6" role="img" aria-label="Adam and Eve beside the tree in the garden"/>
    <text x="115" y="485" text-anchor="middle" class="label-xl">EDEN</text>
  </g>

  <!-- Pre-messiah era -->
  <g class="pre-messiah">
    <text x="232" y="348" text-anchor="middle" class="label" font-size="10">ADAM</text>
    <text x="232" y="360" text-anchor="middle" class="label" font-size="10">REBELLION</text>
    <circle cx="232" cy="407" r="28" fill="var(--red)"/>
    <text x="232" y="412" text-anchor="middle" class="death-text">DEATH</text>

    <circle cx="335" cy="405" r="48" fill="url(#globe)" role="img" aria-label="Globe of the earth"/>
    <text x="335" y="487" text-anchor="middle" class="label-xl">FALLEN EARTH</text>
    <text x="335" y="501" text-anchor="middle" class="label-sub">(PRE-MESSIAH)</text>

    <rect x="418" y="326" width="50" height="38" rx="4" fill="var(--ink)" role="img" aria-label="Tomb on a hill with three crosses"/>
    <circle cx="443" cy="405" r="34" fill="var(--red)"/>
    <text x="443" y="402" text-anchor="middle" class="death-text">JESUS</text>
    <text x="443" y="417" text-anchor="middle" class="death-text">DEATH</text>

    <text transform="translate(511 550) rotate(-90)" class="vertical">JESUS RESURRECTION</text>
  </g>

  <!-- Current era -->
  <g class="current">
    <text x="770" y="238" text-anchor="middle" class="label" font-size="10">HOLY SPIRIT</text>
    <text x="770" y="250" text-anchor="middle" class="label" font-size="10">DESCEND</text>
    <path d="M732 300 h26 l10 52 h-46 z" fill="#fde9a8" opacity=".8"/>
    <rect x="728" y="282" width="34" height="22" rx="8" fill="#cfd6dc" role="img" aria-label="Descending dove"/>

    <circle cx="730" cy="405" r="48" fill="url(#globe)" role="img" aria-label="Globe of the earth"/>
    <text x="730" y="487" text-anchor="middle" class="label-xl">FALLEN EARTH</text>
    <text x="730" y="501" text-anchor="middle" class="label-sub">(CURRENT TIME)</text>

    <circle cx="838" cy="407" r="28" fill="var(--red)"/>
    <text x="838" y="412" text-anchor="middle" class="death-text">DEATH</text>

    <text transform="translate(885 300) rotate(-90)" class="vertical">BELIEVERS</text>
    <text transform="translate(900 280) rotate(-90)" class="vertical">IN JESUS</text>
    <text transform="translate(898 660) rotate(-90)" class="vertical">NON BELIEVERS</text>
    <text x="810" y="185" text-anchor="middle" class="small">THE SAVED</text>
  </g>

  <!-- Hades / Sheol chambers -->
  <g class="hades">
    <text x="248" y="633" text-anchor="middle" class="label" font-size="11">HADES</text>
    <text x="248" y="647" text-anchor="middle" class="label" font-size="11">/SHEOL</text>

    <g clip-path="url(#hadesLeft)">
      <rect x="280" y="570" width="110" height="55" fill="var(--blue)"/>
      <rect x="280" y="625" width="110" height="55" fill="var(--red)"/>
    </g>
    <g clip-path="url(#hadesRight)">
      <rect x="690" y="570" width="110" height="55" fill="var(--blue)"/>
      <rect x="690" y="625" width="110" height="55" fill="var(--red)"/>
    </g>

    <g class="chamber-labels">
      <path d="M335 568 l4 9 10 1 -8 6 3 10 -9 -6 -9 6 3 -10 -8 -6 10 -1z" fill="var(--star)"/>
      <text x="335" y="609" text-anchor="middle" class="white" font-weight="800" font-size="10">PARADISE</text>
      <text x="335" y="618" text-anchor="middle" class="white" font-weight="600" font-size="6.5">(REWARDED)</text>
      <rect x="282" y="623" width="106" height="13" fill="var(--ink)"/>
      <text x="335" y="632.5" text-anchor="middle" class="white" font-weight="800" font-size="7.5">GREAT FIXED GULF</text>
      <text x="335" y="647" text-anchor="middle" class="white" font-weight="800" font-size="10">TORMENT</text>
      <text x="335" y="656" text-anchor="middle" class="white" font-weight="600" font-size="6.5">(CONDEMNED)</text>
      <path d="M335 661 c6 5 9 10 5 16 c-2 3 -8 3 -10 0 c-3 -5 1 -8 2 -11 c1 3 2 4 3 4 c0 -3 -1 -6 0 -9z" fill="var(--star)"/>

      <path d="M745 568 l4 9 10 1 -8 6 3 10 -9 -6 -9 6 3 -10 -8 -6 10 -1z" fill="var(--star)"/>
      <text x="745" y="609" text-anchor="middle" class="white" font-weight="800" font-size="10">PARADISE</text>
      <text x="745" y="618" text-anchor="middle" class="white" font-weight="600" font-size="6.5">(REWARDED)</text>
      <rect x="692" y="623" width="106" height="13" fill="var(--ink)"/>
      <text x="745" y="632.5" text-anchor="middle" class="white" font-weight="800" font-size="7.5">GREAT FIXED GULF</text>
      <text x="745" y="647" text-anchor="middle" class="white" font-weight="800" font-size="10">TORMENT</text>
      <text x="745" y="656" text-anchor="middle" class="white" font-weight="600" font-size="6.5">(CONDEMNED)</text>
      <path d="M745 661 c6 5 9 10 5 16 c-2 3 -8 3 -10 0 c-3 -5 1 -8 2 -11 c1 3 2 4 3 4 c0 -3 -1 -6 0 -9z" fill="var(--star)"/>
    </g>

    <g class="gates">
      <text x="335" y="530" text-anchor="middle" class="small">NARROW</text>
      <text x="335" y="538" text-anchor="middle" class="small">GATE</text>
      <path d="M326 560 v-12 a9 7 0 0 1 18 0 v12 z" fill="none" stroke="var(--blue)" stroke-width="2"/>
      <path d="M331 547 v13 M335 545 v15 M339 547 v13" stroke="var(--blue)" stroke-width="1.3"/>

      <text x="745" y="530" text-anchor="middle" class="small">NARROW</text>
      <text x="745" y="538" text-anchor="middle" class="small">GATE</text>
      <path d="M736 560 v-12 a9 7 0 0 1 18 0 v12 z" fill="none" stroke="var(--blue)" stroke-width="2"/>
      <path d="M741 547 v13 M745 545 v15 M749 547 v13" stroke="var(--blue)" stroke-width="1.3"/>

      <path d="M320 714 v-14 q15 -8 30 0 v14 z" fill="none" stroke="var(--red)" stroke-width="2"/>
      <path d="M325 699 v15 M330 697 v17 M335 696 v18 M340 697 v17 M345 699 v15" stroke="var(--red)" stroke-width="1.3"/>
      <text x="335" y="728" text-anchor="middle" class="small">WIDE</text>
      <text x="335" y="736" text-anchor="middle" class="small">GATE</text>

      <path d="M730 714 v-14 q15 -8 30 0 v14 z" fill="none" stroke="var(--red)" stroke-width="2"/>
      <path d="M735 699 v15 M740 697 v17 M745 696 v18 M750 697 v17 M755 699 v15" stroke="var(--red)" stroke-width="1.3"/>
      <text x="745" y="728" text-anchor="middle" class="small">WIDE</text>
      <text x="745" y="736" text-anchor="middle" class="small">GATE</text>
    </g>
  </g>

  <!-- Flow lines -->
  <g class="flows">
    <!-- pre-messiah saved -->
    <path class="flow-blue" d="M232 437 V545 H316"/>
    <path class="arrow-blue" d="M322 545 l-8 -4 v8 z"/>
    <text x="262" y="539" text-anchor="middle" class="small">THE SAVED</text>
    <path class="flow-blue" d="M232 440 V485"/>
    <path class="arrow-blue" d="M227 488 h10 l-5 7 z"/>
    <path class="flow-blue" d="M335 455 V485"/>
    <path class="arrow-blue" d="M330 488 h10 l-5 7 z"/>
    <path class="flow-blue" d="M443 440 V485"/>
    <path class="arrow-blue" d="M438 488 h10 l-5 7 z"/>
    <path class="flow-blue" d="M443 490 V545 H354"/>
    <path class="arrow-blue" d="M348 545 l8 -4 v8 z"/>
    <!-- resurrection -->
    <path class="flow-blue" d="M390 580 H520 V322"/>
    <path class="arrow-blue" d="M465 576 l8 4 -8 4 z"/>
    <path class="arrow-blue" d="M515 322 h10 l-5 -8 z"/>
    <!-- pre-messiah lost -->
    <path class="flow-red" d="M205 410 V710 H305"/>
    <path class="arrow-red" d="M200 593 h10 l-5 8 z"/>
    <path class="arrow-red" d="M311 710 l-8 -4 v8 z"/>
    <text x="245" y="704" text-anchor="middle" class="small">THE LOST</text>

    <!-- holy spirit -->
    <path class="flow-blue" d="M668 260 H745 V275"/>
    <path class="arrow-blue" d="M740 276 h10 l-5 7 z"/>
    <!-- current earth -->
    <path class="flow-blue" d="M730 455 V485"/>
    <path class="arrow-blue" d="M725 488 h10 l-5 7 z"/>
    <path class="flow-blue" d="M838 437 V545 H764"/>
    <path class="arrow-blue" d="M758 545 l8 -4 v8 z"/>
    <text x="798" y="539" text-anchor="middle" class="small">THE SAVED</text>
    <!-- believers to heaven -->
    <path class="flow-blue" d="M868 400 V180 H680"/>
    <path class="arrow-blue" d="M863 240 h10 l-5 -8 z"/>
    <path class="arrow-blue" d="M674 180 l8 -4 v8 z"/>
    <!-- non believers -->
    <path class="flow-red" d="M868 410 V700 H786"/>
    <path class="arrow-red" d="M863 488 h10 l-5 8 z"/>
    <path class="arrow-red" d="M780 700 l8 -4 v8 z"/>
    <text x="820" y="694" text-anchor="middle" class="small">THE LOST</text>
  </g>
</svg>
</body>
</html>
```